Flyer to Promote Membership in a Trade Association

UPDATE: I am looking for something modern and clean. NO CLIP ART. Not flashy. Just professional and modern. For everyone looking at our current flyer, we don't like it. That's why we aer looking for a new one. So please don't replicate it or use it as inspiration.

I need a flyer to promote membership in the Durable Residence Backers League. It can (probably should) be 2-sided. The content is attached as well as our logo and brand guidelines.

```html
<!DOCTYPE html>
<html lang="en">
<head>
<meta charset="utf-8">
<title>Durable Residence Backers League – Membership Flyer</title>
<link href="https://fonts.googleapis.com/css2?family=Oswald:wght@600;700&family=Montserrat:wght@400;500;600;700;800&display=swap" rel="stylesheet">
<style>
  :root{
    --orange:#f47b2a;
    --slate:#5f6870;
    --ink:#111111;
    --white:#ffffff;
    --backdrop:#3e3e40;
  }
  *{box-sizing:border-box;margin:0;padding:0}
  html,body{width:929px;height:1200px;overflow:hidden;background:var(--backdrop)}
  body{font-family:"Montserrat",sans-serif;color:var(--ink)}
  .sheet{position:relative;width:929px;height:1200px}

  .page{position:absolute;top:298px;width:627px;height:862px;background:var(--white);overflow:hidden;transform:scale(.7);transform-origin:0 0;box-shadow:0 6px 18px rgba(0,0,0,.35)}
  .page-front{left:17px}
  .page-back{left:473px}
  .page > *{position:absolute}

  /* shared */
  .photo{top:0}
  .tick-round svg{width:11px;height:11px}
  .footer-shape{left:0;top:763px;width:627px;height:99px}
  .org{left:67px;top:786px;font-weight:800;font-size:14px;line-height:.95;text-transform:uppercase}
  .address{left:67px;top:818px;font-size:12.5px;font-weight:600;line-height:1.08}
  .pin{left:37px;top:822px;width:17px;height:24px}
  .contact{right:37px;top:804px;text-align:right}
  .contact-row{display:flex;align-items:center;justify-content:flex-end;gap:10px;font-size:17px;line-height:1.35}
  .contact-row.web{font-weight:800}
  .contact-row svg{width:15px;height:15px}

  /* front */
  .brand{left:34px;top:28px;display:flex;align-items:center;gap:10px}
  .brand-square{width:36px;height:36px;background:var(--orange)}
  .brand-name{font-weight:800;font-size:46px;color:var(--slate);line-height:1;letter-spacing:.5px}
  .headline{left:34px;top:108px;font-family:"Oswald",sans-serif;font-weight:700;color:var(--orange);font-size:32px;line-height:1.02}
  .subhead{left:34px;top:218px;font-weight:800;font-size:16.5px;line-height:1.15;color:var(--slate);text-transform:uppercase}
  .intro{left:34px;top:285px;width:250px;font-size:11px;line-height:1.37;font-weight:500}
  .stat{width:180px;display:flex;flex-direction:column;align-items:center}
  .stat-value{font-family:"Oswald",sans-serif;font-weight:700;color:var(--orange);font-size:62px;line-height:1}
  .stat-value sup{font-size:30px;vertical-align:middle}
  .stat-label{font-size:9.5px;font-weight:700;text-transform:uppercase;text-align:center;line-height:1.1;margin-top:2px}
  .stat-1{left:25px;top:416px}
  .stat-2{left:223px;top:416px}
  .stat-3{left:405px;top:408px;width:180px}
  .stat-divider{width:2px;height:93px;top:410px;background:var(--orange)}
  .divider-1{left:219px}
  .divider-2{left:386px}
  .section-title{left:34px;top:540px;font-weight:800;font-size:14.5px;color:var(--orange);text-transform:uppercase}
  .activities{left:34px;top:572px;list-style:none}
  .activities li{display:flex;align-items:center;gap:9px;height:26.5px;font-size:12px;font-weight:600}
  .activities svg{width:20px;height:22px;flex:none}
  .activities .verb{color:var(--orange);font-weight:800;text-transform:uppercase}
  .pitch{left:354px;top:541px;width:250px;font-weight:800;font-size:13.5px;line-height:1.12;color:var(--orange)}
  .join-title{left:354px;top:600px;font-weight:800;font-size:10px;text-transform:uppercase}
  .join-list{left:354px;top:614px;list-style:none}
  .join-list li{display:flex;align-items:center;gap:5px;font-size:7px;font-weight:600;height:14px}
  .join-list li.price{color:var(--orange);font-weight:800;text-transform:uppercase}
  .join-list svg{width:7px;height:7px;flex:none}
  .tier-band{left:0;top:726px;width:627px;height:28px;background:var(--slate);display:flex;align-items:center;padding-left:40px;gap:14px}
  .tier{display:flex;align-items:center;gap:6px;color:var(--white);font-weight:700;font-size:12.5px}
  .tier svg{width:12px;height:12px}

  /* back */
  .benefits-title{left:34px;top:26px;font-family:"Oswald",sans-serif;font-weight:700;color:var(--orange);font-size:31px;line-height:1.1}
  .benefit{left:34px}
  .benefit h3{display:flex;align-items:flex-start;gap:6px;font-weight:800;font-size:12.5px;line-height:1;color:var(--slate);text-transform:uppercase}
  .benefit h3 svg{width:10px;height:10px;flex:none;margin-top:1px}
  .benefit h3 .flag{color:var(--orange);margin-left:6px}
  .benefit p{margin:5px 0 0 5px;font-size:9px;line-height:1.25;font-weight:500}
  .b1{top:88px;width:260px}
  .b2{top:202px;width:260px}
  .b3{top:286px;width:260px}
  .b4{top:367px;width:500px}
  .b5{top:432px;width:520px}
  .b6{top:500px;width:565px}
  .b7{top:566px;width:565px}
  .members-panel{left:0;top:621px;width:627px;height:177px;background:var(--slate)}
  .members-title{left:39px;top:634px;color:var(--white);font-size:10.5px;font-weight:500}
  .members-list{left:39px;top:654px;width:555px;color:var(--white);font-size:8.6px;line-height:1.43;font-weight:500}
  .cta{right:37px;top:752px;color:var(--white);font-size:27px;font-weight:500;line-height:1}
  .cta b{font-weight:800}
  .back-white{left:0;top:798px;width:627px;height:64px;background:var(--white)}
</style>
</head>
<body>
<div class="sheet">

  <!-- FRONT -->
  <section class="page page-front">
    <div class="brand">
      <span class="brand-square"></span>
      <span class="brand-name">DRBL</span>
    </div>

    <svg class="photo" style="left:285px;width:342px;height:405px" viewBox="0 0 342 405" role="img" aria-label="Photo of a hand placing a coin on stacks of coins">
      <defs>
        <linearGradient id="coinTone" x1="0" y1="0" x2="1" y2="1">
          <stop offset="0" stop-color="#e0a25e"/>
          <stop offset=".45" stop-color="#8a6a50"/>
          <stop offset="1" stop-color="#243f58"/>
        </linearGradient>
      </defs>
      <polygon points="70,0 342,0 342,300 185,405 10,280 10,75" fill="var(--orange)"/>
      <polygon points="82,8 342,8 342,292 185,392 22,274 22,80" fill="url(#coinTone)"/>
    </svg>

    <h1 class="headline">Where LIHTC<br>Investing<br>Excellence Begins</h1>
    <p class="subhead">The only community<br>built exclusively<br>for investors</p>
    <p class="intro">DRBL is where federal housing credit investors connect, learn, and lead. We are the only organization solely dedicated to LIHTC investors—giving you a trusted peer network, industry-setting standards, and the insights to stay informed.</p>

    <div class="stat stat-1"><span class="stat-value">30</span><span class="stat-label">Years of impact</span></div>
    <span class="stat-divider divider-1"></span>
    <div class="stat stat-2"><span class="stat-value">60<sup>+</sup></span><span class="stat-label">Investor firms</span></div>
    <span class="stat-divider divider-2"></span>
    <div class="stat stat-3"><span class="stat-value">1,000<sup>+</sup></span><span class="stat-label">Industry<br>professionals</span></div>

    <h2 class="section-title">What members do</h2>
    <ul class="activities">
      <li><svg viewBox="0 0 28 30"><polygon points="14,0 28,8 28,22 14,30 0,22 0,8" fill="var(--orange)"/><circle cx="14" cy="15" r="3" fill="#fff"/><circle cx="7" cy="9" r="2" fill="#fff"/><circle cx="21" cy="9" r="2" fill="#fff"/><circle cx="14" cy="23" r="2" fill="#fff"/></svg><span><span class="verb">Network:</span> Peer Groups &amp; Forums</span></li>
      <li><svg viewBox="0 0 28 30"><polygon points="14,0 28,8 28,22 14,30 0,22 0,8" fill="var(--orange)"/><rect x="8" y="9" width="12" height="13" fill="#fff"/></svg><span><span class="verb">Learn:</span> Conferences &amp; Webinars</span></li>
      <li><svg viewBox="0 0 28 30"><polygon points="14,0 28,8 28,22 14,30 0,22 0,8" fill="var(--orange)"/><path d="M8 21 Q9 13 17 13 L17 9 L22 15 L17 21 L17 17 Q11 17 8 21Z" fill="#fff"/></svg><span><span class="verb">Share:</span> Candid Investor Exchange</span></li>
      <li><svg viewBox="0 0 28 30"><polygon points="14,0 28,8 28,22 14,30 0,22 0,8" fill="var(--orange)"/><path d="M14 8 V22 M7 15 H21 M9 10 L19 20 M19 10 L9 20" stroke="#fff" stroke-width="2.4"/></svg><span><span class="verb">Shape:</span> Standards &amp; Best Practices</span></li>
      <li><svg viewBox="0 0 28 30"><polygon points="14,0 28,8 28,22 14,30 0,22 0,8" fill="var(--orange)"/><rect x="8" y="15" width="3" height="7" fill="#fff"/><rect x="12.5" y="9" width="3" height="13" fill="#fff"/><rect x="17" y="12" width="3" height="10" fill="#fff"/></svg><span><span class="verb">Grow:</span> Professional Development</span></li>
    </ul>

    <p class="pitch">One membership, unlimited access. Your entire team can participate in DRBL activities.</p>
    <h3 class="join-title">Join DRBL today</h3>
    <ul class="join-list">
      <li><svg viewBox="0 0 10 10"><path d="M1 5 L4 8 L9 2" stroke="#111" stroke-width="1.8" fill="none"/></svg>Investor Members</li>
      <li><svg viewBox="0 0 10 10"><path d="M1 5 L4 8 L9 2" stroke="#111" stroke-width="1.8" fill="none"/></svg>Banks, Insurance Companies,</li>
      <li><svg viewBox="0 0 10 10"><path d="M1 5 L4 8 L9 2" stroke="#111" stroke-width="1.8" fill="none"/></svg>Economic Investors</li>
      <li class="price"><svg viewBox="0 0 10 10"><path d="M1 5 L4 8 L9 2" stroke="#111" stroke-width="1.8" fill="none"/></svg>$5,000/year (assets ≥$5B)</li>
      <li class="price"><svg viewBox="0 0 10 10"><path d="M1 5 L4 8 L9 2" stroke="#111" stroke-width="1.8" fill="none"/></svg>$1,000/year (assets &lt;$5B)</li>
    </ul>

    <div class="tier-band">
      <span class="tier"><svg viewBox="0 0 16 16"><circle cx="8" cy="8" r="8" fill="#111"/><path d="M4 8 L7 11 L12 5" stroke="#fff" stroke-width="2" fill="none"/></svg>Affiliate Members</span>
      <span class="tier"><svg viewBox="0 0 16 16"><circle cx="8" cy="8" r="8" fill="#111"/><path d="M4 8 L7 11 L12 5" stroke="#fff" stroke-width="2" fill="none"/></svg>Syndicators &amp; Brokers</span>
      <span class="tier"><svg viewBox="0 0 16 16"><circle cx="8" cy="8" r="8" fill="#111"/><path d="M4 8 L7 11 L12 5" stroke="#fff" stroke-width="2" fill="none"/></svg>$4,500/year</span>
    </div>

    <svg class="footer-shape" viewBox="0 0 627 99" aria-hidden="true"><polygon points="0,0 290,0 400,99 0,99" fill="var(--orange)"/></svg>
    <p class="org">Durable Residence<br>Backers League</p>
    <p class="address">418 Linden Harbor Way, #220<br>Marlow Bend, VA 20991</p>
    <svg class="pin" viewBox="0 0 24 32" aria-hidden="true"><path d="M12 2 C6 2 2 6.5 2 12 C2 19 12 28 12 28 C12 28 22 19 22 12 C22 6.5 18 2 12 2Z" fill="none" stroke="#111" stroke-width="2.6"/><circle cx="12" cy="12" r="3.5" fill="#111"/><rect x="4" y="29" width="16" height="2.5" fill="#111"/></svg>
    <div class="contact">
      <p class="contact-row"><svg viewBox="0 0 20 20"><rect x="1" y="4" width="18" height="12" fill="#111"/><path d="M1 4 L10 11 L19 4" stroke="#fff" stroke-width="1.5" fill="none"/></svg>info@drbl.org</p>
      <p class="contact-row web"><svg viewBox="0 0 20 20"><circle cx="10" cy="10" r="8.5" fill="none" stroke="#111" stroke-width="1.6"/><ellipse cx="10" cy="10" rx="3.5" ry="8.5" fill="none" stroke="#111" stroke-width="1.4"/><path d="M1.5 10 H18.5" stroke="#111" stroke-width="1.4"/></svg>www.drbl.org</p>
    </div>
  </section>

  <!-- BACK -->
  <section class="page page-back">
    <svg class="photo" style="left:312px;width:315px;height:395px" viewBox="0 0 315 395" role="img" aria-label="Photo of business people talking at a meeting table">
      <defs>
        <linearGradient id="meetTone" x1="0" y1="0" x2="1" y2="1">
          <stop offset="0" stop-color="#e6ecf0"/>
          <stop offset=".5" stop-color="#8a97a6"/>
          <stop offset="1" stop-color="#2c3a4e"/>
        </linearGradient>
      </defs>
      <polygon points="110,0 315,0 315,340 235,395 5,255 5,85" fill="var(--orange)"/>
      <polygon points="116,9 315,9 315,334 233,384 14,252 14,90" fill="url(#meetTone)"/>
    </svg>

    <h2 class="benefits-title">Member Benefits</h2>

    <div class="benefit b1"><h3><svg viewBox="0 0 10 10"><circle cx="5" cy="5" r="5" fill="var(--orange)"/><path d="M2.6 5 L4.4 6.8 L7.5 3.4" stroke="#fff" stroke-width="1.3" fill="none"/></svg>Members-only<br>conferences</h3><p>Two annual in-person meetings. Spring Meeting: investors-only for candid peer conversations. Fall Summit: full ecosystem gathering with syndicators and brokers.</p></div>
    <div class="benefit b2"><h3><svg viewBox="0 0 10 10"><circle cx="5" cy="5" r="5" fill="var(--orange)"/><path d="M2.6 5 L4.4 6.8 L7.5 3.4" stroke="#fff" stroke-width="1.3" fill="none"/></svg>Investor-only forums</h3><p>Exclusive meetings and webinars for investors only, enabling candid conversations and meaningful collaboration.</p></div>
    <div class="benefit b3"><h3><svg viewBox="0 0 10 10"><circle cx="5" cy="5" r="5" fill="var(--orange)"/><path d="M2.6 5 L4.4 6.8 L7.5 3.4" stroke="#fff" stroke-width="1.3" fill="none"/></svg>Peer-to-peer meetups</h3><p>Find your peers—underwriters, asset managers, credit officers and more—with our meetups.</p></div>
    <div class="benefit b4"><h3><svg viewBox="0 0 10 10"><circle cx="5" cy="5" r="5" fill="var(--orange)"/><path d="M2.6 5 L4.4 6.8 L7.5 3.4" stroke="#fff" stroke-width="1.3" fill="none"/></svg>Live &amp; on-demand webinars</h3><p>Free monthly Third Thursday webinars covering Year 15 issues,<br>secondary transactions, securitizing developer fees and other emerging topics.</p></div>
    <div class="benefit b5"><h3><svg viewBox="0 0 10 10"><circle cx="5" cy="5" r="5" fill="var(--orange)"/><path d="M2.6 5 L4.4 6.8 L7.5 3.4" stroke="#fff" stroke-width="1.3" fill="none"/></svg>Searchable member directory</h3><p>Find underwriters, asset managers, and credit officers—searchable by role, firm type,<br>and investment approach.</p></div>
    <div class="benefit b6"><h3><svg viewBox="0 0 10 10"><circle cx="5" cy="5" r="5" fill="var(--orange)"/><path d="M2.6 5 L4.4 6.8 L7.5 3.4" stroke="#fff" stroke-width="1.3" fill="none"/></svg>Shape industry standards<span class="flag">[Investor only]</span></h3><p>DRBL's underwriting and asset management standards are adopted industry-wide. Influence<br>them through our committees.</p></div>
    <div class="benefit b7"><h3><svg viewBox="0 0 10 10"><circle cx="5" cy="5" r="5" fill="var(--orange)"/><path d="M2.6 5 L4.4 6.8 L7.5 3.4" stroke="#fff" stroke-width="1.3" fill="none"/></svg>Emerging leaders program<span class="flag">[Investor only]</span></h3><p>Develop your firm's next-generation leaders through dedicated professional development<br>programming.</p></div>

    <div class="members-panel"></div>
    <p class="members-title">Our Investor Members Include</p>
    <p class="members-list">Harborline Life · Kestrel Bank · Meridian Charter National Bank · Bank of Columbia Plains · Corland Trust Bank · Ridgeway Financial · Summitline · Everett Hale Bank · NCTB · Seventh Ward CDC · Grand Townsfolk Bank · Ashford Pell · LatchBank · Weston Crane · Countrywide Mutual · Hudson Crest Life · Vellan (TRAF) · QRT Real Estate · Vista Affordable Housing · Castellan Bank · Hartley Coatings · RV Bank · HamletBank · Fidelis Community Capital · OLM Bank USA · NSMA · Union Bancorp Impact Finance · Stagecoach Ridge Bank</p>
    <p class="cta">Ready to <b>join?</b></p>

    <div class="back-white"></div>
    <svg class="footer-shape" viewBox="0 0 627 99" aria-hidden="true"><polygon points="0,2 313,2 403,99 0,99" fill="var(--orange)"/></svg>
    <p class="org">Durable Residence<br>Backers League</p>
    <p class="address">418 Linden Harbor Way, #220<br>Marlow Bend, VA 20991</p>
    <svg class="pin" viewBox="0 0 24 32" aria-hidden="true"><path d="M12 2 C6 2 2 6.5 2 12 C2 19 12 28 12 28 C12 28 22 19 22 12 C22 6.5 18 2 12 2Z" fill="none" stroke="#111" stroke-width="2.6"/><circle cx="12" cy="12" r="3.5" fill="#111"/><rect x="4" y="29" width="16" height="2.5" fill="#111"/></svg>
    <div class="contact">
      <p class="contact-row"><svg viewBox="0 0 20 20"><rect x="1" y="4" width="18" height="12" fill="#111"/><path d="M1 4 L10 11 L19 4" stroke="#fff" stroke-width="1.5" fill="none"/></svg>info@drbl.org</p>
      <p class="contact-row web"><svg viewBox="0 0 20 20"><circle cx="10" cy="10" r="8.5" fill="none" stroke="#111" stroke-width="1.6"/><ellipse cx="10" cy="10" rx="3.5" ry="8.5" fill="none" stroke="#111" stroke-width="1.4"/><path d="M1.5 10 H18.5" stroke="#111" stroke-width="1.4"/></svg>www.drbl.org</p>
    </div>
  </section>

</div>
</body>
</html>
```